Company identity deisgn should support 2 languages

I would like to get our company identity design
This includes the following only
Business Cards 2 languages Arabic and English
Email signature
Letterhead
Linkedin profile images
Attached is the logo in Ai format

Requirements
Must have
• For business card
Must have
Name and Adrees in arabic
Name and Address in english
You might use both side of the card
Should not have
• Any pictures other than the logo

```html
<!DOCTYPE html>
<html lang="en">
<head>
<meta charset="utf-8">
<title>Cognitive Grid Systems — Stationery</title>
<link href="https://fonts.googleapis.com/css2?family=Montserrat:wght@400;500;700&family=Tajawal:wght@400;500&display=swap" rel="stylesheet">
<style>
  :root {
    --blue: #2680ff;
    --paper: #f2f2f2;
    --backdrop: #cccccc;
    --white: #ffffff;
  }
  * { box-sizing: border-box; margin: 0; padding: 0; }
  html, body { width: 1200px; height: 1128px; overflow: hidden; }
  body {
    background: var(--backdrop);
    position: relative;
    font-family: "Montserrat", sans-serif;
    color: var(--blue);
  }
  .sheet { position: absolute; background: var(--paper); overflow: hidden; }
  .letterhead { left: 88px; top: 75px; width: 686px; height: 983px; }
  .card { width: 283px; height: 162px; left: 847px; }
  .card--en { top: 75px; }
  .card--ar { top: 257px; }

  .wordmark { position: absolute; color: var(--blue); font-weight: 500; line-height: 1; }
  .wordmark__en { display: flex; align-items: center; gap: 6px; letter-spacing: 0.02em; white-space: nowrap; }
  .wordmark__dot { width: 8px; height: 8px; border-radius: 50%; background: var(--blue); flex: none; }
  .wordmark__ar { font-family: "Tajawal", sans-serif; font-weight: 500; direction: rtl; text-align: right; margin-top: 5px; }
  .letterhead .wordmark { left: 222px; top: 36px; }
  .letterhead .wordmark__en { font-size: 18px; }
  .letterhead .wordmark__ar { font-size: 12px; }
  .card .wordmark { left: 140px; top: 14px; }
  .card .wordmark__en { font-size: 8px; gap: 4px; }
  .card .wordmark__dot { width: 5px; height: 5px; }
  .card .wordmark__ar { font-size: 6.5px; margin-top: 3px; }

  .panel { position: absolute; left: 0; bottom: 0; display: block; }
  .letterhead .panel { width: 686px; height: 130px; }
  .card .panel { width: 283px; height: 162px; top: 0; }

  .contact { position: absolute; display: flex; align-items: flex-start; gap: 7px; font-size: 13px; line-height: 16px; }
  .contact .icon { width: 15px; height: 15px; flex: none; }
  .contact--rtl { font-family: "Tajawal", sans-serif; direction: rtl; text-align: right; }

  .letterhead .contact--addr-en { left: 162px; top: 868px; width: 260px; }
  .letterhead .contact--phone { left: 162px; top: 916px; }
  .letterhead .contact--email { left: 162px; top: 947px; }
  .letterhead .contact--addr-ar { right: 36px; top: 868px; width: 230px; font-size: 14px; }
  .letterhead .contact--web { left: 451px; top: 916px; }

  .card .contact { font-size: 8px; line-height: 10.5px; gap: 6px; }
  .card .contact .icon { width: 10px; height: 10px; margin-top: 0.5px; }
  .card--en .contact { left: 164px; }
  .card--en .contact--addr { top: 54px; width: 118px; }
  .card--en .contact--phone { top: 96px; }
  .card--en .contact--email { top: 114px; }
  .card--en .contact--web { top: 131px; }
  .card--ar .contact { right: 11px; }
  .card--ar .contact--addr { top: 67px; width: 160px; font-size: 8.5px; }
  .card--ar .contact--phone { top: 96px; }
  .card--ar .contact--email { top: 114px; }
  .card--ar .contact--web { top: 131px; }
  .card--ar .latin { font-family: "Montserrat", sans-serif; }

  .holder { position: absolute; color: var(--white); }
  .card--en .holder { left: 5px; top: 97px; }
  .card--ar .holder { left: 11px; top: 96px; text-align: left; }
  .holder__name { font-weight: 700; font-size: 8.5px; line-height: 1.1; }
  .card--ar .holder__name { font-family: "Tajawal", sans-serif; font-weight: 500; font-size: 14px; direction: rtl; }
  .holder__title { font-weight: 500; font-size: 6px; line-height: 1.3; }
</style>
</head>
<body>

<svg width="0" height="0" style="position:absolute" aria-hidden="true">
  <defs>
    <symbol id="icon-pin" viewBox="0 0 20 20">
      <circle cx="10" cy="10" r="10" fill="#2680ff"/>
      <path d="M10 4.5a3.8 3.8 0 0 0-3.8 3.8c0 2.8 3.8 7 3.8 7s3.8-4.2 3.8-7A3.8 3.8 0 0 0 10 4.5z" fill="#fff"/>
      <circle cx="10" cy="8.3" r="1.5" fill="#2680ff"/>
    </symbol>
    <symbol id="icon-phone" viewBox="0 0 20 20">
      <circle cx="10" cy="10" r="10" fill="#2680ff"/>
      <path d="M6.3 5.2l2 .1.8 2.4-1.2 1c.6 1.4 1.6 2.4 3 3l1-1.2 2.4.8.1 2c-.1.6-.6 1-1.2 1C9 14.1 5.9 11 5.6 6.4c0-.6.3-1.1.7-1.2z" fill="#fff"/>
    </symbol>
    <symbol id="icon-mail" viewBox="0 0 20 20">
      <circle cx="10" cy="10" r="10" fill="#2680ff"/>
      <rect x="5" y="6.5" width="10" height="7" rx="1" fill="#fff"/>
      <path d="M5.5 7l4.5 3.5L14.5 7" stroke="#2680ff" stroke-width="1" fill="none"/>
    </symbol>
    <symbol id="icon-web" viewBox="0 0 20 20">
      <circle cx="10" cy="10" r="10" fill="#2680ff"/>
      <circle cx="10" cy="10" r="4.8" stroke="#fff" stroke-width="1.2" fill="none"/>
      <path d="M5.2 10h9.6M10 5.2c-2 2.6-2 7 0 9.6M10 5.2c2 2.6 2 7 0 9.6" stroke="#fff" stroke-width="1" fill="none"/>
    </symbol>
  </defs>
</svg>

<!-- Letterhead -->
<section class="sheet letterhead" aria-label="Letterhead">
  <div class="wordmark">
    <div class="wordmark__en"><span class="wordmark__dot"></span>COGNITIVE GRID SYSTEMS</div>
    <div class="wordmark__ar">شركة أنظمة الشبكة المعرفية</div>
  </div>

  <svg class="panel" viewBox="0 0 686 130" preserveAspectRatio="none" aria-hidden="true">
    <path d="M0 0H40L120 120H686V130H0Z" fill="var(--blue)"/>
  </svg>

  <div class="contact contact--addr-en"><svg class="icon"><use href="#icon-pin"/></svg><span>Nakheel tower 12th floor Prince Faisal st. Dammam Saudi Arabia</span></div>
  <div class="contact contact--phone"><svg class="icon"><use href="#icon-phone"/></svg><span>966500000000</span></div>
  <div class="contact contact--email"><svg class="icon"><use href="#icon-mail"/></svg><span>info@cognigrid.sa</span></div>
  <div class="contact contact--rtl contact--addr-ar" lang="ar"><svg class="icon"><use href="#icon-pin"/></svg><span>برج النخيل الدور ١٢ شارع الأمير فيصل، الدمام السعودية</span></div>
  <div class="contact contact--web"><svg class="icon"><use href="#icon-web"/></svg><span>www.cognigrid.sa</span></div>
</section>

<!-- Business card, English -->
<section class="sheet card card--en" aria-label="Business card, English">
  <svg class="panel" viewBox="0 0 283 162" preserveAspectRatio="none" aria-hidden="true">
    <path d="M0 0H62L150 150H283V162H0Z" fill="var(--blue)"/>
  </svg>
  <div class="wordmark">
    <div class="wordmark__en"><span class="wordmark__dot"></span>COGNITIVE GRID SYSTEMS</div>
    <div class="wordmark__ar">شركة أنظمة الشبكة المعرفية</div>
  </div>
  <div class="holder">
    <div class="holder__name">Khalid Alharbi</div>
    <div class="holder__title">Business Development Director</div>
  </div>
  <div class="contact contact--addr"><svg class="icon"><use href="#icon-pin"/></svg><span>Nakheel tower 12th floor Prince Faisal st. Dammam Saudi Arabia</span></div>
  <div class="contact contact--phone"><svg class="icon"><use href="#icon-phone"/></svg><span>966500000000</span></div>
  <div class="contact contact--email"><svg class="icon"><use href="#icon-mail"/></svg><span>info@cognigrid.sa</span></div>
  <div class="contact contact--web"><svg class="icon"><use href="#icon-web"/></svg><span>www.cognigrid.sa</span></div>
</section>

<!-- Business card, Arabic -->
<section class="sheet card card--ar" aria-label="Business card, Arabic" lang="ar">
  <svg class="panel" viewBox="0 0 283 162" preserveAspectRatio="none" aria-hidden="true">
    <path d="M0 0H62L150 150H283V162H0Z" fill="var(--blue)"/>
  </svg>
  <div class="wordmark" lang="en">
    <div class="wordmark__en"><span class="wordmark__dot"></span>COGNITIVE GRID SYSTEMS</div>
    <div class="wordmark__ar" lang="ar">شركة أنظمة الشبكة المعرفية</div>
  </div>
  <div class="holder">
    <div class="holder__name">خالد الحربي</div>
    <div class="holder__title" lang="en">Business Development Director</div>
  </div>
  <div class="contact contact--rtl contact--addr"><svg class="icon"><use href="#icon-pin"/></svg><span>برج النخيل الدور ١٢ شارع الأمير فيصل، الدمام السعودية</span></div>
  <div class="contact contact--rtl contact--phone"><svg class="icon"><use href="#icon-phone"/></svg><span class="latin" dir="ltr">966500000000</span></div>
  <div class="contact contact--rtl contact--email"><svg class="icon"><use href="#icon-mail"/></svg><span class="latin" dir="ltr">info@cognigrid.sa</span></div>
  <div class="contact contact--rtl contact--web"><svg class="icon"><use href="#icon-web"/></svg><span class="latin" dir="ltr">www.cognigrid.sa</span></div>
</section>

</body>
</html>
```